Webpage for a treatment housing for young addicts.

I need a new design and files for my wordpress page. I need it to be more neat and clean. I need it to look professional with a starting page that will work as a navigation. I need like logo and phone number and such up top, a picture under it with one sentence as a slogan and under it 6 boxes to click to come to our different pages. Under it I want news etc.

Target Market(s)

Social services, employees and governements

Coding

Coded - Design and coding required

Font styles to use
Sans Serif

Colors
abd037
3176b5
9d9d9d
aaaaaa
f04a50

Requirements
Must have
• A nice design
Nice to have
• need it to look professional with a starting page that will work as a navigation. I need like logo and phone number and such up top, a picture under it with one sentence as a slogan and under it 6 boxes to click to come to our different pages. Under it I want news etc.
• today www.kelmora.se
• want more like www.trivest.se or www.solbrink.se
Should not have
• To many different colours and a messy design.

```html
<!DOCTYPE html>
<html lang="en">
<head>
<meta charset="utf-8">
<title>Kelmora – Home</title>
<link href="https://fonts.googleapis.com/css2?family=Jost:wght@400;500;600&family=Oswald:wght@500&display=swap" rel="stylesheet">
<style>
:root{
  --red:#f04a50;
  --blue:#0b80d0;
  --blue-dark:#1a6db3;
  --ink:#2b2f36;
  --muted:#8a8d93;
  --grey-band:#e8eaee;
  --line:#e1e3e7;
  --panel:#45494f;
  --white:#fff;
}
*{box-sizing:border-box;margin:0;padding:0}
html,body{width:1200px;height:3103px;overflow:hidden}
body{font-family:"Jost",Arial,sans-serif;color:var(--ink);background:var(--white);position:relative}
a{color:inherit;text-decoration:none}

/* header */
.site-header{position:absolute;left:0;top:0;width:1200px;height:80px;background:var(--white);z-index:3}
.brand{position:absolute;left:83px;top:18px;display:flex;align-items:center;gap:10px;font-weight:600;font-size:30px;color:var(--blue);line-height:1}
.brand-dot{width:34px;height:34px;border-radius:50%;background:#abd037}
.header-tools{position:absolute;left:648px;top:0;display:flex;height:80px}
.tool{height:80px;border-left:1px solid var(--line);display:flex;align-items:center;justify-content:center;flex-direction:column;gap:3px}
.tool-call{width:207px;flex-direction:row;gap:12px}
.tool-call small{display:block;color:var(--red);font-size:13px;line-height:1}
.tool-call strong{font-family:"Oswald",sans-serif;font-weight:500;font-size:19px;line-height:1.1}
.tool-mail{width:107px;font-size:12px}
.tool-search{width:83px;font-size:12px}
.tool-close{width:75px;background:#eef0f3}

/* dropdown */
.nav-drop{position:absolute;left:888px;top:80px;width:232px;height:359px;background:var(--white);z-index:3;padding:18px 22px 0}
.nav-drop li{list-style:none;font-size:14px;font-weight:500;height:47.5px;line-height:47.5px;border-bottom:1px solid var(--line)}
.nav-drop li:first-child{height:40px;line-height:40px}
.nav-drop li.active{color:var(--red)}
.nav-drop li:last-child{border:none}
.drop-social{display:flex;gap:9px;margin-top:6px}
.drop-social span{width:22px;height:22px;border:1.5px solid var(--red);border-radius:50%}

/* hero */
.hero{position:absolute;left:0;top:80px;width:1200px;height:359px;background:linear-gradient(110deg,#c9b49b 0%,#9c8672 35%,#7a6b5e 60%,#b9a893 100%)}
.hero-slogan{position:absolute;left:0;width:1200px;top:135px;text-align:center;color:var(--white);font-size:37px;font-weight:500;line-height:43px}
.hero-arrow{position:absolute;left:592px;top:305px}

/* quick nav */
.quick-nav{position:absolute;left:0;top:439px;width:1200px;height:271px;background:var(--grey-band)}
.nav-box{position:absolute;width:334px;height:64px;background:var(--white);display:flex;align-items:center;justify-content:space-between;padding:0 22px;font-size:15px;font-weight:500}
.nav-box.active{color:var(--red);box-shadow:0 6px 14px rgba(0,0,0,.08)}
.arrow-ring{width:20px;height:20px;border:1.5px solid var(--red);border-radius:50%;display:flex;align-items:center;justify-content:center}

/* intro */
.intro{position:absolute;left:0;top:710px;width:1200px;height:380px;text-align:center}
.intro h1{position:absolute;left:0;width:1200px;top:64px;font-size:23px;font-weight:500;line-height:31px}
.intro p{position:absolute;left:258px;width:684px;top:146px;font-size:13.5px;line-height:20.5px;color:var(--muted)}
.btn{position:absolute;height:33px;font-size:12px;display:flex;align-items:center;justify-content:center;color:var(--red);border:1.5px solid var(--red);background:var(--white)}
.btn.solid{background:var(--red);color:var(--white)}

/* feature cards */
.features{position:absolute;left:0;top:1090px;width:1200px;height:340px;background:var(--blue)}
.feature{position:absolute;top:67px;width:320px;height:200px}
.feature-label{position:absolute;left:24px;right:24px;bottom:22px;color:var(--white);font-size:14px;font-weight:500;display:flex;justify-content:space-between}
.feature-label.underlined span:first-child{text-decoration:underline}

/* two columns */
.split{position:absolute;left:0;top:1430px;width:1200px;height:360px}
.split-col{position:absolute;top:92px;width:480px;text-align:center}
.split-col h2{font-size:35px;font-weight:500;line-height:44px}
.split-col p{margin:18px auto 0;width:380px;font-size:12.5px;line-height:19px;color:var(--muted)}
.split-divider{position:absolute;left:600px;top:40px;width:1px;height:290px;background:var(--line)}

/* locations */
.locator{position:absolute;left:81px;top:1831px;width:1039px;height:238px;background:var(--panel);text-align:center;color:var(--white)}
.locator h2{margin-top:45px;font-size:35px;font-weight:500;line-height:42px}
.locator p{font-size:13px;margin-top:2px}
.select{position:absolute;top:149px;width:267px;height:37px;background:var(--white);color:var(--muted);font-size:12px;display:flex;align-items:center;justify-content:space-between;padding:0 14px;text-align:left}
.locator .btn{top:149px;height:37px;border:none}

/* news */
.news-head{position:absolute;left:0;width:1200px;top:2128px;text-align:center}
.news-head h2{font-size:35px;font-weight:500;line-height:44px}
.news-head p{font-size:13px}
.article{position:absolute;top:2228px;width:320px;height:317px;background:#f2f3f5;text-align:center}
.article-photo{height:199px}
.article time{display:block;margin-top:26px;font-size:12px}
.article h3{margin-top:10px;font-size:15px;font-weight:500;line-height:20px;color:var(--blue-dark)}
.article h3.hover{text-decoration:underline}
.pager{position:absolute;left:572px;top:2577px;display:flex;gap:8px}
.pager span{width:12px;height:12px;border:1.5px solid var(--red);border-radius:50%}
.pager span.on{background:radial-gradient(var(--red) 35%,transparent 40%)}

/* footer */
.site-footer{position:absolute;left:0;top:2721px;width:1200px;height:382px;background:var(--blue);color:var(--white)}
.foot-col{position:absolute;top:58px;font-size:13px;line-height:23px}
.foot-col h4{font-size:16px;font-weight:500;margin-bottom:24px}
.foot-phone{font-family:"Oswald",sans-serif;font-size:19px;font-weight:500}
.newsletter{margin-top:14px;width:237px;height:30px;background:rgba(255,255,255,.35);font-size:11px;display:flex;align-items:center;justify-content:space-between;padding:0 12px}
.foot-bar{position:absolute;left:0;top:304px;width:1200px;height:1px;background:rgba(255,255,255,.3)}
.copyright{position:absolute;left:81px;top:332px;font-size:13px}
.follow{position:absolute;left:615px;top:328px;display:flex;align-items:center;gap:8px;font-size:13px}
.follow span.ring{width:25px;height:25px;border:1.5px solid var(--white);border-radius:50%}
.to-top{position:absolute;left:1100px;top:330px}
</style>
</head>
<body>

<header class="site-header">
  <a class="brand" href="#"><span class="brand-dot"></span>Kelmora</a>
  <div class="header-tools">
    <div class="tool tool-call">
      <svg width="22" height="22" viewBox="0 0 24 24" fill="none" stroke="#f04a50" stroke-width="2"><path d="M5 3h4l2 5-3 2a12 12 0 0 0 6 6l2-3 5 2v4a2 2 0 0 1-2 2A17 17 0 0 1 3 5a2 2 0 0 1 2-2z"/></svg>
      <div><small>Call Us:</small><strong>010-4827360</strong></div>
    </div>
    <div class="tool tool-mail">
      <svg width="22" height="16" viewBox="0 0 22 16" fill="none" stroke="#f04a50" stroke-width="1.8"><rect x="1" y="1" width="20" height="14"/><path d="M1 1l10 8 10-8"/></svg>
      <span>info@kelmora.se</span>
    </div>
    <div class="tool tool-search">
      <svg width="22" height="22" viewBox="0 0 22 22" fill="none" stroke="#f04a50" stroke-width="2"><circle cx="9" cy="9" r="7"/><path d="M14 14l6 6"/></svg>
      <span>Search</span>
    </div>
    <div class="tool tool-close">
      <svg width="24" height="24" viewBox="0 0 24 24" stroke="#f04a50" stroke-width="2"><path d="M3 3l18 18M21 3L3 21"/></svg>
    </div>
  </div>
</header>

<section class="hero" role="img" aria-label="Photo of a child playing with a toy car at a table">
  <p class="hero-slogan">We create sustainable roads<br>to a better future</p>
  <svg class="hero-arrow" width="16" height="24" viewBox="0 0 16 24" fill="none" stroke="#fff" stroke-width="2"><path d="M8 2v19M3 16l5 5 5-5"/></svg>
</section>

<nav class="nav-drop">
  <ul>
    <li>Personal assistance</li>
    <li class="active">Individual and family</li>
    <li>LSS</li>
    <li>Elderly care</li>
    <li>About Kelmora</li>
    <li>Investor</li>
  </ul>
  <div class="drop-social"><span></span><span></span><span></span></div>
</nav>

<section class="quick-nav">
  <a class="nav-box" style="left:81px;top:64px">Personal assistance<span class="arrow-ring"><svg width="10" height="10" viewBox="0 0 10 10" fill="none" stroke="#f04a50" stroke-width="1.5"><path d="M1 5h8M5 1l4 4-4 4"/></svg></span></a>
  <a class="nav-box active" style="left:432px;top:64px">Individual and family<span class="arrow-ring"><svg width="10" height="10" viewBox="0 0 10 10" fill="none" stroke="#f04a50" stroke-width="1.5"><path d="M1 5h8M5 1l4 4-4 4"/></svg></span></a>
  <a class="nav-box" style="left:786px;top:64px">LSS<span class="arrow-ring"><svg width="10" height="10" viewBox="0 0 10 10" fill="none" stroke="#f04a50" stroke-width="1.5"><path d="M1 5h8M5 1l4 4-4 4"/></svg></span></a>
  <a class="nav-box" style="left:81px;top:145px">Elderly care<span class="arrow-ring"><svg width="10" height="10" viewBox="0 0 10 10" fill="none" stroke="#f04a50" stroke-width="1.5"><path d="M1 5h8M5 1l4 4-4 4"/></svg></span></a>
  <a class="nav-box" style="left:432px;top:145px">About Kelmora<span class="arrow-ring"><svg width="10" height="10" viewBox="0 0 10 10" fill="none" stroke="#f04a50" stroke-width="1.5"><path d="M1 5h8M5 1l4 4-4 4"/></svg></span></a>
  <a class="nav-box" style="left:786px;top:145px">Investor<span class="arrow-ring"><svg width="10" height="10" viewBox="0 0 10 10" fill="none" stroke="#f04a50" stroke-width="1.5"><path d="M1 5h8M5 1l4 4-4 4"/></svg></span></a>
</section>

<section class="intro">
  <h1>Kelmora Sverige AB carries out care and care aimed<br>at people aged 14-25 years.</h1>
  <p>Kelmora Sverige AB carries out care and care aimed at people aged 14-25 years. This is done primarily through Home for care and housing (HVB) . We are specialists in psychosocial abuse and crime issues. By being constantly open to new methods and aware of the existing ones, we develop and improve our care. The methods are adapted to the individual, we do not think that ONE thought or ONE perspective can be applied to everyone ...</p>
  <a class="btn" href="#" style="left:534px;top:285px;width:130px">Discover more</a>
</section>

<section class="features">
  <a class="feature" href="#" style="left:81px;background:linear-gradient(160deg,#8aa65a,#5f7a3e 55%,#3d4a2c)" role="img" aria-label="Photo of a group of young people outdoors">
    <span class="feature-label"><span>The team</span><span>›</span></span>
  </a>
  <a class="feature" href="#" style="left:439px;background:linear-gradient(160deg,#6b5448,#4a3a33 60%,#2f2623)" role="img" aria-label="Photo of a carer helping an older person">
    <span class="feature-label underlined"><span>Quality work</span><span>→</span></span>
  </a>
  <a class="feature" href="#" style="left:799px;background:linear-gradient(160deg,#8a5a3a,#6e3f28 55%,#3f2a1f)" role="img" aria-label="Photo of a mother and daughter gardening">
    <span class="feature-label"><span>Valuation &amp; Ethical Approach</span><span>›</span></span>
  </a>
</section>

<section class="split">
  <div class="split-col" style="left:100px">
    <h2>Ekbacka farm<br>HVB</h2>
    <p>Close to Malmö, Lund and Helsingborg lies Ekbackagården beautifully situated in the small village of Norrbacka surrounded by beautiful nature and rolling fields ...</p>
  </div>
  <div class="split-divider"></div>
  <div class="split-col" style="left:620px">
    <h2>In-depth description of<br>treatment.</h2>
    <p>The basis for treatment is a well-structured therapeutic treatment and housing environment, where the therapeutic environment becomes an active treatment layer ...</p>
  </div>
  <a class="btn" href="#" style="left:276px;top:262px;width:126px">Explore more</a>
  <a class="btn solid" href="#" style="left:796px;top:262px;width:128px">Explore more</a>
</section>

<section class="locator">
  <h2>We are located all over sweden!</h2>
  <p>There are many variations of passages of Lorem Ipsum</p>
  <div class="select" style="left:159px">Select country<span>⌄</span></div>
  <div class="select" style="left:451px">Choose service<span>⌄</span></div>
  <a class="btn solid" href="#" style="left:742px;width:135px">Search</a>
</section>

<div class="news-head">
  <h2>Recent articles</h2>
  <p>There are many variations of passages of Lorem Ipsum</p>
</div>
<article class="article" style="left:81px">
  <div class="article-photo" role="img" aria-label="Photo of a mother and child building with toy blocks" style="background:linear-gradient(150deg,#c7d6e3,#a9b8c4 50%,#d7a54a)"></div>
  <time>November 13, 2018</time>
  <h3>Contrary to popular belief,Ipsum<br>is not simply</h3>
</article>
<article class="article" style="left:440px">
  <div class="article-photo" role="img" aria-label="Photo of a carer with an older woman" style="background:linear-gradient(150deg,#e8e4df,#bdb2a6 55%,#8b7c70)"></div>
  <time>October 18, 2018</time>
  <h3>Contrary to popular belief,Ipsum<br>is not simply</h3>
</article>
<article class="article" style="left:800px">
  <div class="article-photo" role="img" aria-label="Photo of a nurse serving tea to an older woman" style="background:linear-gradient(150deg,#d9d4cc,#a89f93 55%,#6e6458)"></div>
  <time>October 15, 2018</time>
  <h3 class="hover">Contrary to popular belief,Ipsum<br>is not simply</h3>
</article>
<div class="pager"><span></span><span class="on"></span><span></span></div>
<a class="btn solid" href="#" style="left:534px;top:2623px;width:130px;height:34px">View all news</a>

<footer class="site-footer">
  <div class="foot-col" style="left:81px">
    <h4>Contact us</h4>
    <div class="foot-phone">Call us: 010-4827360</div>
    <div>Email: info@kelmora.se</div>
    <div style="margin-top:10px;font-weight:500">Visit us:</div>
    <div>Norrbacka 2207 41530 Lindhult</div>
  </div>
  <div class="foot-col" style="left:348px">
    <h4>Quick links</h4>
    <div>Personal assistance</div>
    <div style="text-decoration:underline">Individual and family</div>
    <div>LSS</div>
    <div>Elderly care</div>
    <div>About Kelmora</div>
    <div>Investor</div>
  </div>
  <div class="foot-col" style="left:615px">
    <h4>About Kelmora</h4>
    <div>The team</div>
    <div>Quality work</div>
    <div>Valuation &amp; Ethical Approach</div>
    <div>News</div>
    <div>Contact Us</div>
  </div>
  <div class="foot-col" style="left:883px">
    <h4>Sign up newsletter</h4>
    <div style="line-height:18px">Sign up now &amp; get Update about<br>anything News!</div>
    <div class="newsletter"><span>Enter your email ...</span><span>→</span></div>
  </div>
  <div class="foot-bar"></div>
  <div class="copyright">© 2018 Kelmora. All rights reserved.</div>
  <div class="follow">Follow Us: <span class="ring"></span><span class="ring"></span><span class="ring"></span></div>
  <svg class="to-top" width="20" height="20" viewBox="0 0 20 20" fill="none" stroke="#fff" stroke-width="2"><path d="M3 17L10 3l7 14"/></svg>
</footer>

</body>
</html>
```